Refresh Home Page for Photography Training Site

http://brannowlessons.example/

My site is looking kind of out-of-date, so it's time for a face lift. I want to bring it up to date with a more modern web look.

What I need from you is a home page design concept. No coding, just a PSD design, but it MUST be something that a coder could build into an efficient, fast-loading page. After the home page design contest is finished, we can work together privately, if you want to continue, to design the rest of the pages in the site for additional fees.

Functionally, the new page needs to do the same job as the current home page, just do it more efficiently (if possible) while looking fresh and modern.

Sites I like
http://quelt.example/ (clean, modern)

Competitor sites:
http://varnocourses.example/
http://www.ivanmorrowimaging.example/

Target Market(s)

Amateur and semi-professional photographers

Industry/Entity Type

Training

Requirements
Must have
• MUST HAVE
1. A prominent space where testimonials appear in rotation, one after another (instead of the one large testimonial on the current site).

2. My photo in the header. It can be smaller than at present. If you prefer you can use the black and white photo from the about page. Put a signature saying Dan Brannow near the photo, in a better handwritten style than the current signature, which is a lame font.

3. Tagline "Learn Photography and Image Editing the Easy Way"
Should not have
• No flash or other fancy technology. (However it is acceptable to design an area that would be an image carousel, where one image changes to another, then another, etc. Like the Ivan Morrow or Quelt site. That is not too fancy, but it's optional).

```html
<!DOCTYPE html>
<html lang="en">
<head>
<meta charset="utf-8">
<title>Brannow Training – Learn Photography and Image Editing the Easy Way</title>
<link rel="stylesheet" href="https://fonts.googleapis.com/css2?family=Maven+Pro:wght@400;500;700&family=Arimo:wght@400;700&family=Great+Vibes&family=Kaushan+Script&display=swap">
<style>
:root{
  --black:#000;
  --band-top:#2c5f8c;
  --band-bottom:#1b4770;
  --white:#fff;
  --ink:#222;
  --muted:#555;
  --rule:#cfcfcf;
  --card-bg:#f0f0f0;
  --card-border:#d6d6d6;
  --link:#1a4f86;
  --accent:#0a5a9c;
  --slide-top:#0c94d2;
  --slide-bottom:#0a5c9c;
  --slide-text:#d2e9f7;
  --script:#5fd0f4;
  --footer:#1f4a72;
  --footer-dark:#0f2236;
  --footer-text:#dbe6f0;
}
*{box-sizing:border-box;margin:0;padding:0}
html,body{width:934px;height:1200px;overflow:hidden;background:var(--white)}
body{position:relative;font-family:"Arimo",Arial,sans-serif;color:var(--ink)}
a{color:inherit}
.abs{position:absolute}

/* top bar */
.topbar{left:0;top:0;width:934px;height:78px;background:var(--black)}
.portrait{left:0;top:0;width:205px;height:78px;background:radial-gradient(circle at 90px 40px,#5a6f86 0,#2b3440 45px,#0d0f12 80px,#000 110px)}
.signature{left:112px;top:50px;font-family:"Great Vibes",cursive;font-size:22px;color:var(--white)}
.tagline{left:300px;top:15px;width:400px;text-align:center;font-family:"Maven Pro",sans-serif;font-weight:700;font-size:16px;line-height:22px;color:var(--white)}
.camera{left:690px;top:0;width:200px;height:78px;background:linear-gradient(90deg,#000 0,#2a2a2a 40%,#111 100%)}

/* header band */
.band{left:0;top:78px;width:934px;height:302px;background:linear-gradient(180deg,var(--band-top),var(--band-bottom))}
.brand{left:65px;top:110px;width:235px;white-space:nowrap;font-family:"Maven Pro",sans-serif;font-size:26px;line-height:32px;font-weight:400;color:var(--white)}
.nav{left:313px;top:106px;width:557px;height:42px;border-radius:10px;background:linear-gradient(180deg,#fff,#dcdcdc);box-shadow:0 2px 4px rgba(0,0,0,.35);display:flex;overflow:hidden}
.nav a{display:flex;align-items:center;justify-content:center;text-decoration:none;font-family:"Maven Pro",sans-serif;font-size:12.5px;font-weight:500;color:#333;border-right:1px solid #c9c9c9;height:100%}
.nav a:last-child{border-right:0}
.nav .active{background:linear-gradient(180deg,#fff,#f4f4f4);color:#111}

/* slider */
.slider-frame{left:75px;top:173px;width:785px;height:267px;background:#eef3f7;box-shadow:0 6px 12px rgba(0,0,0,.25)}
.slide{left:81px;top:180px;width:772px;height:253px;background:radial-gradient(circle at 60% 30%,var(--slide-top),var(--slide-bottom) 90%)}
.slide-title{left:108px;top:214px;font-family:"Maven Pro",sans-serif;font-size:18px;font-weight:400;color:var(--white)}
.slide-text{left:108px;top:250px;width:360px;font-family:"Maven Pro",sans-serif;font-size:10.5px;line-height:18.5px;color:var(--slide-text)}
.slide-script{left:146px;top:333px;font-family:"Kaushan Script",cursive;font-size:22px;color:var(--script)}
.slide-art{left:490px;top:200px;width:200px;height:160px;border-radius:50%;background:radial-gradient(ellipse,rgba(190,215,240,.55),rgba(60,120,180,0) 70%)}
.slide-dots{left:826px;top:222px;width:14px}
.slide-dots span{display:block;width:10px;height:10px;margin:0 0 16px 2px;border-radius:50%;background:#dbeaf5}
.slide-dots span.on{width:13px;height:13px;margin-left:0;background:#7fb3d8;border:2px solid #e8f2fa}
.slide-arrows{left:92px;top:403px}

/* testimonial */
.rule{height:1px;background:var(--rule);left:60px;width:814px}
.quote-open{left:108px;top:478px;font-family:Georgia,serif;font-size:34px;font-weight:700;font-style:italic;line-height:34px;color:#888}
.quote{left:133px;top:486px;width:700px;font-family:"Maven Pro",sans-serif;font-size:14.5px;line-height:29px;color:#555}
.quote .mark{font-family:Georgia,serif;font-size:30px;font-weight:700;font-style:italic;line-height:10px;color:#888;vertical-align:-8px;margin-left:8px}
.quote .author{color:var(--accent);font-size:15px;margin-left:14px}
.q-arrow{top:507px}

/* cards */
.card{width:175px;height:212px;background:var(--card-bg);border:1px solid var(--card-border)}
.card h3{position:absolute;left:10px;top:9px;font-family:"Maven Pro",sans-serif;font-size:14px;font-weight:500;color:#111}
.card .line{position:absolute;left:6px;right:0;top:37px;height:1px;background:#c8c8c8}
.card .thumb{position:absolute;left:7px;top:47px;width:158px;height:84px;border:1px solid #bbb}
.card p{position:absolute;left:7px;top:137px;width:158px;font-size:9.5px;line-height:17px;text-align:justify;color:#111}
.card .more{position:absolute;right:10px;top:190px;font-size:9.5px;color:var(--link)}

/* sidebar */
.side-title{font-family:"Maven Pro",sans-serif;font-size:14px;font-weight:500;color:#111}
.side-rule{left:623px;width:264px;height:1px;background:var(--rule)}
.pager{font-size:14px;font-weight:700;color:#1a6fb0;letter-spacing:1px}
.tut-thumb{width:77px;height:62px;border:1px solid #ccc}
.tut-text{width:172px;font-size:9.5px;line-height:17px;text-align:justify;color:#111}
.tut-more{font-size:9.5px;color:var(--link)}
.works{left:623px;top:867px;width:264px;height:155px;background:#f2f2f2;border:1px solid var(--card-border)}
.works-head{left:624px;top:868px;width:262px;height:33px;background:linear-gradient(180deg,#fafafa,#e6e6e6);border-bottom:1px solid #d0d0d0}
.works-thumb{width:78px;height:48px;border:1px solid #bbb}

/* footer */
.footer{left:0;top:1043px;width:934px;height:95px;background:var(--footer)}
.foot-col h4{font-family:"Maven Pro",sans-serif;font-size:11px;font-weight:700;color:var(--white);padding-bottom:6px;border-bottom:1px solid #4d7398;width:165px}
.foot-col{top:1053px;font-size:8.5px;line-height:12px;color:var(--footer-text)}
.foot-links{display:flex;gap:22px;margin-top:6px}
.foot-links ul{list-style:none}
.newsletter input{width:120px;height:18px;border:1px solid #aaa;background:#fff;margin-top:12px}
.newsletter button{height:18px;font-size:9px;font-family:"Arimo",Arial,sans-serif;background:linear-gradient(#f4f4f4,#cfcfcf);border:1px solid #888;padding:0 3px}
.social{display:flex;gap:12px;margin-top:12px}
.social span{width:25px;height:25px;border-radius:50%;background:var(--white)}
.bottom{left:0;top:1138px;width:934px;height:62px;background:var(--footer-dark);text-align:center;font-size:9.5px;line-height:14px;color:#c7d2dd;padding-top:15px}
</style>
</head>
<body>

<header>
  <div class="abs topbar"></div>
  <div class="abs portrait" role="img" aria-label="Portrait photo of Dan Brannow framed by a camera lens ring"></div>
  <div class="abs signature">Dan Brannow</div>
  <p class="abs tagline">Learn Photography and<br>Image Editing the Easy Way</p>
  <div class="abs camera" role="img" aria-label="Photo of a black DSLR camera"></div>

  <div class="abs band"></div>
  <div class="abs brand">Brannow Training</div>
  <nav class="abs nav">
    <a class="active" href="#" style="width:83px">Home</a>
    <a href="#" style="width:74px">Courses</a>
    <a href="#" style="width:123px">Free Tutorials</a>
    <a href="#" style="width:93px">About Us</a>
    <a href="#" style="width:101px">Contact Us</a>
    <a href="#" style="width:83px">Log In</a>
  </nav>
</header>

<section aria-label="Featured carousel">
  <div class="abs slider-frame"></div>
  <div class="abs slide"></div>
  <h2 class="abs slide-title">Lorem Ipsum Contantry</h2>
  <p class="abs slide-text">The standard chunk of Lorem Ipsum used since the 1500s is reproduced below for those interested. Sections 1.10.32 and 1.10.33 from "de Finibus Bonorum et Malorum" by Orelius are also reproduced in their exact original form, accompanied by English</p>
  <div class="abs slide-script">Lorem Ipsum Contantry</div>
  <div class="abs slide-art" role="img" aria-label="Photo of a striped tropical fish in blue water"></div>
  <div class="abs slide-dots"><span class="on"></span><span></span><span></span><span></span><span></span><span></span><span></span></div>
  <svg class="abs slide-arrows" width="48" height="20" viewBox="0 0 48 20" aria-hidden="true">
    <rect x="0" y="0" width="20" height="19" rx="3" fill="#e6eef4"/>
    <path d="M12 5 L7 9.5 L12 14Z" fill="#1c5d93"/>
    <rect x="27" y="0" width="20" height="19" rx="3" fill="#e6eef4"/>
    <path d="M35 5 L40 9.5 L35 14Z" fill="#1c5d93"/>
  </svg>
</section>

<section aria-label="Testimonials">
  <div class="abs rule" style="top:471px"></div>
  <svg class="abs q-arrow" style="left:73px" width="16" height="18" viewBox="0 0 16 18" aria-hidden="true"><path d="M12 2 L5 9 L12 16" fill="none" stroke="#999" stroke-width="3"/></svg>
  <span class="abs quote-open" aria-hidden="true">“</span>
  <p class="abs quote">Orelius are also reproduced in their exact original form,"de Finibus Bonorum et Malorum" accompanied by English versions from the 1914 translation by H. Wendell.<span class="mark">”</span><span class="author">- Mel Jarrow</span></p>
  <svg class="abs q-arrow" style="left:843px" width="16" height="18" viewBox="0 0 16 18" aria-hidden="true"><path d="M4 2 L11 9 L4 16" fill="none" stroke="#999" stroke-width="3"/></svg>
  <div class="abs rule" style="top:556px"></div>
</section>

<main>
  <article class="abs card" style="left:43px;top:579px">
    <h3>Photography Tips</h3><div class="line"></div>
    <div class="thumb" role="img" aria-label="Photo of a tiger leaping through snow" style="background:linear-gradient(135deg,#cfd8e6,#e9edf3 50%,#c88a4a)"></div>
    <p>Orelius are also reproduced in their exact original form, accompanied by English versions.</p>
    <a class="more" href="#">View more</a>
  </article>
  <article class="abs card" style="left:233px;top:579px">
    <h3>Photography Tricks</h3><div class="line"></div>
    <div class="thumb" role="img" aria-label="Photo of fire and flames in orange tones" style="background:radial-gradient(circle at 40% 50%,#f6b233,#c8410d 60%,#3a0b02)"></div>
    <p>Orelius are also reproduced in their exact original form, accompanied by English versions.</p>
    <a class="more" href="#">View more</a>
  </article>
  <article class="abs card" style="left:424px;top:579px">
    <h3>Event Photos</h3><div class="line"></div>
    <div class="thumb" role="img" aria-label="Photo of a swimmer beneath a grey sea wave" style="background:linear-gradient(180deg,#5c6a70,#a8b6b9 50%,#3f6a6a)"></div>
    <p>Orelius are also reproduced in their exact original form, accompanied by English versions.</p>
    <a class="more" href="#">View more</a>
  </article>

  <article class="abs card" style="left:43px;top:813px">
    <h3>Photography Tips</h3><div class="line"></div>
    <div class="thumb" role="img" aria-label="Photo of a lemon splashing into blue water" style="background:radial-gradient(circle at 50% 60%,#f2d43a 0,#e0b820 18%,#1a5fb0 40%,#0b2f6e)"></div>
    <p>Orelius are also reproduced in their exact original form, accompanied by English versions.</p>
    <a class="more" href="#">View more</a>
  </article>
  <article class="abs card" style="left:233px;top:813px">
    <h3>Photography Tricks</h3><div class="line"></div>
    <div class="thumb" role="img" aria-label="Black and white photo of a cyclist on a curved ramp" style="background:linear-gradient(135deg,#2a2a2a,#bdbdbd 55%,#e8e8e8)"></div>
    <p>Orelius are also reproduced in their exact original form, accompanied by English versions.</p>
    <a class="more" href="#">View more</a>
  </article>
  <article class="abs card" style="left:424px;top:813px">
    <h3>Event Photos</h3><div class="line"></div>
    <div class="thumb" role="img" aria-label="Underwater photo of a diver holding a lantern" style="background:radial-gradient(circle at 40% 60%,#7aa86a,#1b7f86 50%,#0b3c4a)"></div>
    <p>Orelius are also reproduced in their exact original form, accompanied by English versions.</p>
    <a class="more" href="#">View more</a>
  </article>
</main>

<aside>
  <h3 class="abs side-title" style="left:624px;top:589px">Free Photo Tutorials</h3>
  <span class="abs pager" style="left:857px;top:588px">‹›</span>
  <div class="abs side-rule" style="top:616px"></div>

  <div class="abs tut-thumb" role="img" aria-label="Photo of a camera lens" style="left:625px;top:626px;background:linear-gradient(135deg,#f4f4f4,#8a8a8a 60%,#dcdcdc)"></div>
  <p class="abs tut-text" style="left:709px;top:624px">Orelius are also reproduced in their exact original form, accompanied by English versions.</p>
  <a class="abs tut-more" style="left:836px;top:677px" href="#">View more</a>

  <div class="abs tut-thumb" role="img" aria-label="Photo of a small ornament on a blue background" style="left:625px;top:703px;background:radial-gradient(circle,#8fa6c4,#2b4f94 70%)"></div>
  <p class="abs tut-text" style="left:709px;top:701px">Orelius are also reproduced in their exact original form, accompanied by English versions.</p>
  <a class="abs tut-more" style="left:836px;top:754px" href="#">View more</a>

  <div class="abs tut-thumb" role="img" aria-label="Photo of a bird perched on a glass bowl" style="left:625px;top:780px;background:linear-gradient(135deg,#ececec,#b9a98a 55%,#6f8a4c)"></div>
  <p class="abs tut-text" style="left:709px;top:778px">Orelius are also reproduced in their exact original form, accompanied by English versions.</p>
  <a class="abs tut-more" style="left:836px;top:831px" href="#">View more</a>

  <div class="abs works"></div>
  <div class="abs works-head"></div>
  <h3 class="abs side-title" style="left:630px;top:875px">My Other Works</h3>
  <span class="abs pager" style="left:857px;top:874px">‹›</span>
  <div class="abs works-thumb" role="img" aria-label="Black and white photo" style="left:630px;top:911px;background:linear-gradient(135deg,#ddd,#777)"></div>
  <div class="abs works-thumb" role="img" aria-label="Landscape photo at golden hour" style="left:716px;top:911px;background:linear-gradient(135deg,#d49a3a,#5b4a24)"></div>
  <div class="abs works-thumb" role="img" aria-label="Misty nature photo" style="left:802px;top:911px;background:linear-gradient(135deg,#c7c8b0,#6f7550)"></div>
  <div class="abs works-thumb" role="img" aria-label="Photo of a person outdoors" style="left:630px;top:967px;background:linear-gradient(180deg,#9fb8cf,#4a4a3a)"></div>
  <div class="abs works-thumb" role="img" aria-label="Photo of a pink sunset coastline" style="left:716px;top:967px;background:linear-gradient(180deg,#e7b9a8,#9a6f70)"></div>
  <div class="abs works-thumb" role="img" aria-label="Photo of a glowing light bulb in the dark" style="left:802px;top:967px;background:radial-gradient(circle,#f1b23d,#2a1604 45%,#000)"></div>
</aside>

<footer>
  <div class="abs footer"></div>
  <div class="abs foot-col" style="left:44px">
    <h4>Menu</h4>
    <div class="foot-links">
      <ul><li>Home</li><li>Courses</li><li>Free Tutorials</li><li>About Us</li></ul>
      <ul><li>Contact Us</li><li>Log in</li><li>Register</li><li>Sitemap</li></ul>
    </div>
  </div>
  <div class="abs foot-col" style="left:258px">
    <h4>Latest from the Blog</h4>
    <p style="margin-top:6px;width:165px">Orelius are also reproduced in their exact original form, accompanied by English versions.</p>
    <p style="text-align:right;width:158px;margin-top:2px"><a href="#">View more</a></p>
  </div>
  <div class="abs foot-col newsletter" style="left:472px">
    <h4>News Letter</h4>
    <input type="text" aria-label="Email address"><button type="button">Subscribe</button>
  </div>
  <div class="abs foot-col" style="left:685px">
    <h4>Connect with us</h4>
    <div class="social" aria-label="Social links"><span></span><span></span><span></span><span></span><span></span></div>
  </div>
  <div class="abs bottom">Copyright © 2011 brannowlessons.example All rights reserved<br>Terms and conditions &nbsp;|&nbsp; Privacy policy</div>
</footer>

</body>
</html>
```